Business Cards Design - Steady Harbor Builders

Need business card designs with logo attached to the file for the revamp of my old business. Looking for that solid professional business card design that is better than the guy who came before me and the guy that come after me. Modern, simple, easy to get the important information without having to guess which numbers to call. Looking to see all ideas also want to see some designs with matte colors with the shiny popping color.

Business card designs speak a lot about the efforts you put into your business that you are promising to consumers that you care about their stuff or properties as much as you care about your own. If you dont even care about the smalll things, how are you going to care about the big things!!

Target Market(s)

Property owners, Property managers, Homeowner owners, Business Owners, Other contractors.

Industry/Entity Type

Roofing / Storm Restoration

Contact Information for Business Card

Name, Phone #, Email , Social Media Icons, QR Code

Requirements
Must have
• Premium looks that stands out and looks top notch

```html
<!DOCTYPE html>
<html lang="en">
<head>
<meta charset="utf-8">
<title>Steady Harbor Builders – Business Card</title>
<link rel="stylesheet" href="https://fonts.googleapis.com/css2?family=Montserrat:wght@400;600;700&display=swap">
<style>
  :root {
    --stage: #c9c9c9;
    --card: #231f20;
    --card-deep: #1a1718;
    --ink: #ffffff;
    --ink-soft: #e6e6e6;
    --accent: #e31e24;
    --social-a: #3b5998;
    --social-b: #a23a8c;
    --social-c: #e31e24;
  }
  * { box-sizing: border-box; margin: 0; padding: 0; }
  html, body {
    width: 1200px; height: 800px; overflow: hidden;
    background: var(--stage);
    font-family: "Montserrat", sans-serif;
  }
  .stage {
    width: 1200px; height: 800px;
    display: flex; align-items: center; justify-content: center; gap: 40px;
  }
  .card {
    position: relative;
    width: 540px; height: 309px;
    background: var(--card);
    border: 2px solid var(--accent);
    overflow: hidden;
  }

  /* Front */
  .brand {
    position: absolute; left: 44px; top: 50%; transform: translateY(-50%);
    display: flex; align-items: center; gap: 12px;
  }
  .brand__mark { width: 12px; height: 12px; background: var(--accent); flex: none; }
  .brand__name {
    color: var(--ink); font-weight: 600; font-size: 20px;
    letter-spacing: 0.14em; text-transform: uppercase; line-height: 1.35;
    width: 200px;
  }
  .divider {
    position: absolute; left: 280px; top: 70px; width: 1px; height: 100px;
    background: linear-gradient(to bottom, transparent, #8a8a8a, transparent);
  }
  .contact { position: absolute; left: 306px; top: 78px; color: var(--ink); }
  .contact__name {
    font-weight: 700; font-size: 17px; letter-spacing: 0.05em;
    text-transform: uppercase; margin-bottom: 16px;
  }
  .contact__row {
    display: flex; align-items: center; gap: 8px;
    font-size: 14px; font-weight: 400; color: var(--ink-soft); margin-bottom: 6px;
  }
  .contact__row svg { width: 14px; height: 14px; flex: none; }
  .social {
    position: absolute; left: 306px; bottom: 60px; display: flex; gap: 8px;
  }
  .social span { width: 18px; height: 18px; border-radius: 50%; }
  .social .s1 { background: var(--social-a); }
  .social .s2 { background: var(--social-b); }
  .social .s3 { background: var(--social-c); }

  /* Back */
  .pattern {
    position: absolute; inset: 0;
    background: radial-gradient(ellipse at 60% 40%, #2c2829 0%, var(--card) 55%, var(--card-deep) 100%);
  }
  .back-brand {
    position: absolute; left: 50%; top: 50%; transform: translate(-50%, -50%);
    display: flex; align-items: center; gap: 10px;
  }
  .back-brand .brand__name { font-size: 15px; width: auto; white-space: nowrap; }
  .back-brand .brand__mark { width: 9px; height: 9px; }
</style>
</head>
<body>
<main class="stage">
  <section class="card card--front" aria-label="Card front">
    <div class="brand">
      <span class="brand__mark"></span>
      <p class="brand__name">Steady Harbor Builders</p>
    </div>
    <div class="divider"></div>
    <div class="contact">
      <p class="contact__name">Marcus Hale</p>
      <p class="contact__row">
        <svg viewBox="0 0 24 24" aria-hidden="true"><path fill="#e31e24" d="M6.6 10.8a15 15 0 0 0 6.6 6.6l2.2-2.2c.3-.3.7-.4 1-.2 1.1.4 2.3.6 3.6.6.6 0 1 .4 1 1V20c0 .6-.4 1-1 1A17 17 0 0 1 3 4c0-.6.4-1 1-1h3.5c.6 0 1 .4 1 1 0 1.3.2 2.5.6 3.6.1.3 0 .7-.2 1z"/></svg>
        044-555 018 246
      </p>
      <p class="contact__row">
        <svg viewBox="0 0 24 24" aria-hidden="true"><path fill="#e31e24" d="M2 5h20v14H2z"/><path fill="none" stroke="#231f20" stroke-width="1.6" d="M2 5l10 8 10-8"/></svg>
        hello@harborbuild.net
      </p>
    </div>
    <div class="social" aria-label="Social media">
      <span class="s1"></span><span class="s2"></span><span class="s3"></span>
    </div>
  </section>

  <section class="card card--back" aria-label="Card back">
    <div class="pattern" role="img" aria-label="Faint tone-on-tone repeated company wordmark pattern"></div>
    <div class="back-brand">
      <span class="brand__mark"></span>
      <p class="brand__name">Steady Harbor Builders</p>
    </div>
  </section>
</main>
</body>
</html>
```